Emergency Vehicle Installer and Security Firm Needs a Business Card

Our company "Corvalta" need a business card for our Emergency Vehicle Equipment Installation and Infrastructure Security Business. We are contract designers, manufacturers and installers for Emergency Vehicle Fleets. This includes installation of Emergency Lights, Sirens, Vehicle Graphics and Radio Communications. We also supply this products to an international market. We also do consultant, and installation of high level security access, alarm and surveillance equipment for medium to large size businesses.

The design should represent a level of trust in our professionalism and expertise. It should visually display our ongoing relationship with the emergency services, but not overtake our commitment to high level security options.

Target Market(s)

Emergency Services and Businesses requiring high level security

Industry/Entity Type

Business

Contact Information for Business Card

*note complete details will be given to the winning designer for revising. The name "Mark Pelling will be used to fill in name".

Mark Pelling
Managing Director
Corvalta NZ Limited
Phone: +64 027 846 20193
Email: mark.pelling@corvalta-example.co.nz

Requirements
Must have
• Card must be in black. Using our logo on the top as supplied. Designers should try having the reverse side as a blurred image of police lights (red and blue) with our logo in greyscale in the centre (this is not particularly a requirement, but feel free to play around with this option).
Nice to have
• A card design that looks good when spot UV printed. A clean compact and graphic design. A grey scale feel on the front (excluding logo, but you can play around with that idea). Rounded smooth text.
Should not have
• Will update this section as designs come through - feel free to submit what you feel would look good.

```html
<!DOCTYPE html>
<html lang="en">
<head>
<meta charset="utf-8">
<title>Corvalta Business Card</title>
<link href="https://fonts.googleapis.com/css2?family=Open+Sans:wght@400;600;700;800&display=swap" rel="stylesheet">
<style>
  :root {
    --stage: #1a1817;
    --card: #1e1e1f;
    --card-back: #232324;
    --red: #e3232b;
    --white: #f4f4f4;
    --grey: #bdbdbd;
    --uv-grey: #4a4a4c;
  }
  * { margin: 0; padding: 0; box-sizing: border-box; }
  html, body { width: 1200px; height: 716px; overflow: hidden; background: var(--stage); }
  body { position: relative; font-family: "Open Sans", Arial, sans-serif; }

  .card {
    position: absolute;
    width: 520px;
    height: 297px;
    overflow: hidden;
    box-shadow: 0 18px 40px rgba(0,0,0,.55);
  }
  .card--front { left: 50px; top: 210px; background: var(--card); }
  .card--back { left: 630px; top: 210px; background: var(--card-back); }

  .card__graphics { position: absolute; inset: 0; }

  .brand {
    position: absolute;
    display: flex;
    align-items: center;
    gap: 10px;
  }
  .brand__name {
    font-weight: 800;
    font-size: 34px;
    letter-spacing: 1px;
    color: var(--white);
    line-height: 1;
  }
  .brand__mark { width: 14px; height: 14px; background: var(--red); }
  .card--front .brand { left: 34px; top: 30px; }

  .company {
    position: absolute;
    left: 26px;
    top: 112px;
    font-size: 11px;
    line-height: 1.45;
    color: var(--grey);
  }
  .company__name { color: var(--red); font-weight: 700; }

  .person {
    position: absolute;
    left: 300px;
    top: 128px;
  }
  .person__name { color: var(--red); font-weight: 700; font-size: 15px; letter-spacing: .5px; }
  .person__role { color: var(--grey); font-size: 11px; margin-top: 2px; }

  .contacts {
    position: absolute;
    left: 300px;
    top: 190px;
    list-style: none;
    font-size: 11px;
    color: var(--grey);
  }
  .contacts li { display: flex; align-items: center; gap: 8px; margin-bottom: 5px; }
  .contacts svg { width: 11px; height: 11px; flex: none; }

  .website {
    position: absolute;
    right: 24px;
    bottom: 8px;
    font-size: 11px;
    font-weight: 600;
    color: var(--white);
  }

  .card--back .brand {
    left: 50%;
    top: 50%;
    transform: translate(-50%, -50%);
  }
  .card--back .brand__name { font-size: 52px; color: var(--uv-grey); letter-spacing: 2px; }
  .card--back .brand__mark { width: 18px; height: 18px; }
</style>
</head>
<body>

  <section class="card card--front" aria-label="Business card front">
    <svg class="card__graphics" viewBox="0 0 520 297" aria-hidden="true">
      <polyline points="0,88 240,88 278,126 520,126" fill="none" stroke="#e3232b" stroke-width="1.2"/>
      <polygon points="0,226 0,236 180,297 215,297" fill="#f4f4f4"/>
      <polygon points="195,262 520,262 520,297 230,297" fill="#e3232b"/>
    </svg>

    <div class="brand">
      <span class="brand__name">CORVALTA</span>
      <span class="brand__mark"></span>
    </div>

    <address class="company" style="font-style: normal;">
      <div class="company__name">Corvalta NZ Limited</div>
      <div>1100 Harbour Street</div>
      <div>Any where, Any City</div>
    </address>

    <div class="person">
      <div class="person__name">MARK PELLING</div>
      <div class="person__role">Managing Director</div>
    </div>

    <ul class="contacts">
      <li>
        <svg viewBox="0 0 12 12"><rect width="12" height="12" rx="2" fill="#e3232b"/><path d="M3.5 2.5l1.5 0 .6 1.8-.9.7a5 5 0 0 0 2.3 2.3l.7-.9 1.8.6v1.5c0 .4-.3.7-.7.7A6.5 6.5 0 0 1 2.8 3.2c0-.4.3-.7.7-.7z" fill="#fff"/></svg>
        <span>+64 027 846 20193</span>
      </li>
      <li>
        <svg viewBox="0 0 12 12"><rect width="12" height="12" rx="2" fill="#e3232b"/><rect x="2.5" y="3.5" width="7" height="5" fill="none" stroke="#fff" stroke-width=".9"/><polyline points="2.5,3.5 6,6.3 9.5,3.5" fill="none" stroke="#fff" stroke-width=".9"/></svg>
        <span>mark.pelling@corvalta-example.co.nz</span>
      </li>
    </ul>

    <div class="website">www.corvalta-example.co.nz</div>
  </section>

  <section class="card card--back" aria-label="Business card back">
    <div class="brand">
      <span class="brand__name">CORVALTA</span>
      <span class="brand__mark"></span>
    </div>
  </section>

</body>
</html>
```